Business Card Design Project

Need a business card designed for a horse racing/gambling centered company.
Company name is PebbleLark.com.au
Company colours are similar to those in the logo.
Something clean and modern , designer given liberty to be creative.
Incorporate the logo is preferred.
Single or Double Sided fine
Must include :
Name
Mobile Number
Email Address
Reason: Apologies, I have been traveling unexpectedly with business and just need the extra two days to reply and give feedback before making a decision.

```html
<!DOCTYPE html>
<html lang="en">
<head>
<meta charset="utf-8">
<title>PebbleLark.com.au — Business Card</title>
<link rel="stylesheet" href="https://fonts.googleapis.com/css2?family=Open+Sans:wght@300;400;600&display=swap">
<style>
  :root {
    --page-bg: #e9e6e1;
    --card-teal: #1ea898;
    --card-teal-light: #2bb9a8;
    --card-teal-dark: #168f82;
    --accent-lime: #c9dc1c;
    --text-white: #ffffff;
    --divider: rgba(255,255,255,0.55);
    --mark-fill: #ffffff;
  }
  * { box-sizing: border-box; margin: 0; padding: 0; }
  html, body { width: 1200px; height: 900px; overflow: hidden; }
  body {
    background: var(--page-bg);
    font-family: "Open Sans", Arial, sans-serif;
    color: var(--text-white);
    display: flex;
    flex-direction: column;
    align-items: center;
    justify-content: center;
    gap: 40px;
  }
  .card {
    position: relative;
    width: 700px;
    height: 400px;
    border-radius: 4px;
    background: radial-gradient(ellipse at 35% 30%, var(--card-teal-light), var(--card-teal) 55%, var(--card-teal-dark));
    box-shadow: 0 6px 18px rgba(0,0,0,0.18);
    overflow: hidden;
  }
  .brand {
    position: absolute;
    display: flex;
    align-items: center;
    gap: 16px;
  }
  .brand-dot {
    width: 62px; height: 62px;
    border-radius: 50%;
    background: var(--mark-fill);
    flex-shrink: 0;
  }
  .brand-name {
    font-weight: 300;
    font-size: 40px;
    letter-spacing: -0.5px;
    color: var(--text-white);
    white-space: nowrap;
  }
  /* front */
  .card-front .brand { left: 90px; top: 140px; }
  .front-rule {
    position: absolute;
    left: 250px; top: 232px;
    width: 215px; height: 3px;
    background: linear-gradient(90deg, rgba(255,255,255,0), var(--divider));
  }
  .front-web {
    position: absolute;
    left: 478px; top: 222px;
    font-size: 15px;
    font-weight: 600;
    white-space: nowrap;
  }
  /* back */
  .card-back .brand { left: 50px; top: 110px; }
  .holder { position: absolute; left: 60px; top: 250px; }
  .holder-name { font-size: 36px; font-weight: 400; line-height: 1.1; }
  .holder-role { font-size: 22px; font-weight: 400; color: var(--accent-lime); }
  .back-divider {
    position: absolute;
    left: 345px; top: 205px;
    width: 2px; height: 110px;
    background: linear-gradient(180deg, rgba(255,255,255,0), var(--divider), rgba(255,255,255,0));
  }
  .contact {
    position: absolute;
    left: 375px; top: 200px;
    font-size: 17px;
    font-weight: 600;
    line-height: 1.25;
    white-space: nowrap;
  }
  .contact-address { margin-bottom: 6px; }
  .contact-list { list-style: none; }
  .contact-list li { display: flex; align-items: center; gap: 12px; height: 26px; }
  .contact-icon { width: 18px; height: 18px; flex-shrink: 0; }
</style>
</head>
<body>

  <section class="card card-front" aria-label="Business card front">
    <div class="brand">
      <span class="brand-dot"></span>
      <span class="brand-name">PebbleLark.com.au</span>
    </div>
    <div class="front-rule"></div>
    <p class="front-web">www.pebblelark.com.au</p>
  </section>

  <section class="card card-back" aria-label="Business card back">
    <div class="brand">
      <span class="brand-dot"></span>
      <span class="brand-name">PebbleLark.com.au</span>
    </div>

    <div class="holder">
      <p class="holder-name">Alex Carter</p>
      <p class="holder-role">Owner</p>
    </div>

    <div class="back-divider"></div>

    <div class="contact">
      <p class="contact-address">1408 /62 Harbour Lane<br>Sydney, NSW , 2001</p>
      <ul class="contact-list">
        <li>
          <svg class="contact-icon" viewBox="0 0 18 18" aria-hidden="true">
            <rect width="18" height="18" rx="2" fill="var(--accent-lime)"/>
            <path d="M5 4h2.5l1 3-1.5 1a7 7 0 0 0 3 3l1-1.5 3 1V13a1.5 1.5 0 0 1-1.5 1.5A9 9 0 0 1 3.5 5.5 1.5 1.5 0 0 1 5 4z" fill="var(--card-teal-dark)"/>
          </svg>
          <span>1300 555 318</span>
        </li>
        <li>
          <svg class="contact-icon" viewBox="0 0 18 18" aria-hidden="true">
            <rect width="18" height="18" rx="2" fill="var(--accent-lime)"/>
            <rect x="3.5" y="5" width="11" height="8" fill="none" stroke="var(--card-teal-dark)" stroke-width="1.5"/>
            <path d="M3.5 5l5.5 4.5L14.5 5" fill="none" stroke="var(--card-teal-dark)" stroke-width="1.5"/>
          </svg>
          <span>info@pebblelark.com.au</span>
        </li>
        <li>
          <svg class="contact-icon" viewBox="0 0 18 18" aria-hidden="true">
            <rect width="18" height="18" rx="2" fill="var(--accent-lime)"/>
            <circle cx="9" cy="9" r="5.5" fill="none" stroke="var(--card-teal-dark)" stroke-width="1.5"/>
            <path d="M3.5 9h11M9 3.5c-2 2-2 9 0 11M9 3.5c2 2 2 9 0 11" fill="none" stroke="var(--card-teal-dark)" stroke-width="1.2"/>
          </svg>
          <span>www.pebblelark.com.au</span>
        </li>
      </ul>
    </div>
  </section>

</body>
</html>
```